Catalogue design for Aluminium Panel and spray painting manufacturer based in Huizhou, China.

Metrovex is a trading company that represent Dansheng metal spraying industry that manufactures aluminium panels and extrusions of all kinds and PVDF coating.

We are a manufacturer and producer of aluminium panels and PVDF painting based in Huizhou, China. We produce aluminium panels that are use widely in subways, shopping malls and construction works both for interior and exterior usage.

Dan Sheng mainly deal with contractors and project managers business within Mainland China and Hong Kong with a select few clientele in Australia and Philippines. We are now looking to expand the business and reach further international businesses.

We therefore need a new brochure to introduce the new trading name Metrovex to further the sales strategy into international borders. As manufacturers are heavily based on credentials and certifications these must be displayed accordingly to gain trust within the construction market.

The following content will be required

1. Who we are and what we do, manufacturer of aluminium panels and PVDF coating.
2. a)Guide to our manufacturing process, bending, cutting, welding of aluminum panels
b)Guide to choice of painting powder coating or PVDF coating. (PVDF being the main choice)
3. a)Some technical information about the core product of aluminium of aluminum panels such as size dimensions, width of panels and grade of aluminium.
b)Information on PVDF painting and a colour chart of either RAL or PANTONE.
4. Projects undertaken and some photos, preferably in a grid 2 column layout as exampled on attached photo.
5. Certifications of factory and office address and contact info.

We are looking for design that can showcase our manufacturing process in a catalogue displaying a consistent colour design theme throughout.

A simple guide of the manufacturing process and including some technical specification about the aluminium panels such as width and maximum dimenstions etc.

Target Market(s)

Asean and south east asia.

Industry/Entity Type

Manufacturer

Contact Information for Business Card

To be in colour theme with the catalogue design. Contain logo and to draw more focus more on the web url.

Colors
ec1f27

Requirements
Must have
• Must include a colour theme that is striking throughout the catalogue and easy to look at graphical layout. A graphical view without too much text aside from the technical specifications.
• Certifications of manufacturer. ISO, Verlo Danth etc( as displayed within company profile PDF)
Nice to have
• A consistent usage of photos without too obvious generic building photos.
• A well displayed layout for each page.
• Perhaps a three toned colour theme that works according with the logo. Perhaps some red throughout on a black main colour. Contrasting colours without an overwash of one colour.
Should not have
• Generic photos of office people or overly enthusiastic business people.
• With Exception of photos shots of the factory workers.

```html
<!DOCTYPE html>
<html lang="en">
<head>
<meta charset="utf-8">
<title>Metrovex Catalogue – Machine &amp; Quality Process</title>
<link href="https://fonts.googleapis.com/css2?family=Libre+Baskerville:wght@700&family=Open+Sans:wght@400;600;700&display=swap" rel="stylesheet">
<style>
  :root{
    --page-bg:#e8e8ea;
    --maroon:#7a0f14;
    --maroon-dark:#4a0508;
    --ink:#1b1b1b;
    --white:#ffffff;
    --brand-red:#b5121b;
    --flow-red:#e2334a;
    --flow-green:#a6cf3b;
    --flow-blue:#3d92d6;
    --flow-teal:#1b98a6;
    --flow-cyan:#4cc3cf;
    --flow-orange:#ef7a2c;
    --flow-purple:#3b1c4a;
    --line:#1e1e1e;
  }
  *{margin:0;padding:0;box-sizing:border-box}
  html,body{width:1200px;height:464px;overflow:hidden;background:var(--page-bg)}
  .spread{position:relative;width:1200px;height:464px;display:flex;font-family:"Open Sans",sans-serif}
  .page{position:relative;width:600px;height:464px;background:var(--page-bg);overflow:hidden}
  .page-art{position:absolute;inset:0}
  .page-title{position:absolute;left:238px;top:18px;font-family:"Libre Baskerville",serif;font-weight:700;font-size:28px;letter-spacing:1px;color:var(--white)}
  .footer{position:absolute;left:0;right:0;bottom:0;height:40px}
  .brand{position:absolute;bottom:18px;display:flex;align-items:center;gap:4px;font-family:"Open Sans",sans-serif;font-weight:700;font-size:12px;color:var(--brand-red)}
  .brand-mark{width:14px;height:14px;background:var(--brand-red)}
  .footer-rule{position:absolute;bottom:22px;height:3px;display:flex;gap:4px}
  .footer-rule span{flex:1;background:var(--ink)}
  .page-number{position:absolute;bottom:0;width:40px;height:40px;background:var(--ink);color:var(--white);font-size:20px;font-weight:600;display:flex;align-items:center;justify-content:center;overflow:hidden}
  .page-number::before{content:"";position:absolute;left:0;top:0;border-top:10px solid var(--brand-red);border-right:10px solid transparent}
  .flow text{font-family:"Open Sans",sans-serif;font-size:4.6px;fill:var(--white);text-anchor:middle;font-weight:600}
  .flow .label{fill:var(--ink);font-weight:700;font-size:5.5px;text-anchor:start}
  .flow .hex-text{font-family:"Libre Baskerville",serif;font-weight:400}
  .flow .conn{stroke:var(--line);stroke-width:1.6;fill:none}
</style>
</head>
<body>
<main class="spread">
  <!-- Page 3: machinery -->
  <section class="page page-machine">
    <svg class="page-art" width="600" height="464" viewBox="0 0 600 464">
      <defs>
        <linearGradient id="band" x1="0" y1="0" x2="1" y2="1">
          <stop offset="0" stop-color="#8e141a"/><stop offset="1" stop-color="#3e0407"/>
        </linearGradient>
        <linearGradient id="machineGreen" x1="0" y1="0" x2="1" y2="1">
          <stop offset="0" stop-color="#b8c96a"/><stop offset="1" stop-color="#6f7d3a"/>
        </linearGradient>
        <linearGradient id="machineGrey" x1="0" y1="0" x2="1" y2="1">
          <stop offset="0" stop-color="#a7aeb5"/><stop offset="1" stop-color="#4e5359"/>
        </linearGradient>
        <linearGradient id="machineBlue" x1="0" y1="0" x2="1" y2="1">
          <stop offset="0" stop-color="#5f82b8"/><stop offset="1" stop-color="#2f4f86"/>
        </linearGradient>
        <linearGradient id="machineBrown" x1="0" y1="0" x2="1" y2="1">
          <stop offset="0" stop-color="#9a7a70"/><stop offset="1" stop-color="#4c2a25"/>
        </linearGradient>
        <linearGradient id="machineDark" x1="0" y1="0" x2="1" y2="1">
          <stop offset="0" stop-color="#8c9aa3"/><stop offset="1" stop-color="#3b4147"/>
        </linearGradient>
        <linearGradient id="laserRed" x1="0" y1="0" x2="0" y2="1">
          <stop offset="0" stop-color="#6f7a78"/><stop offset="0.6" stop-color="#4d5553"/><stop offset="1" stop-color="#a8232b"/>
        </linearGradient>
      </defs>
      <polygon points="0,0 176,0 0,136" fill="var(--ink)"/>
      <polygon points="0,0 160,0 0,122" fill="url(#band)"/>
      <polygon points="150,0 445,0 300,122" fill="url(#band)"/>
      <g stroke="#fff" stroke-width="3">
        <polygon role="img" aria-label="Photo: operator at a press brake with an open machine frame" points="0,140 165,300 0,460" fill="url(#machineDark)"/>
        <polygon role="img" aria-label="Photo: green hydraulic press brake in the workshop" points="185,0 325,140 185,280 45,140" fill="url(#machineGreen)"/>
        <polygon role="img" aria-label="Photo: long press brake line seen at an angle" points="440,20 570,150 440,280 310,150" fill="url(#machineGrey)"/>
        <polygon role="img" aria-label="Photo: press brake machine with warm lighting" points="505,150 625,270 505,390 385,270" fill="url(#machineBrown)"/>
        <polygon role="img" aria-label="Photo: blue CNC bending machine" points="300,170 430,300 300,430 170,300" fill="url(#machineBlue)"/>
        <polygon role="img" aria-label="Photo: red laser cutting machine bed" points="175,285 305,415 175,545 45,415" fill="url(#laserRed)"/>
      </g>
    </svg>
    <h1 class="page-title">MACHINE</h1>
    <footer class="footer">
      <div class="brand" style="left:26px"><span class="brand-mark"></span>Metrovex</div>
      <div class="footer-rule" style="left:104px;width:428px"><span></span><span></span><span></span><span></span><span></span><span></span><span></span></div>
      <div class="page-number" style="left:541px">3</div>
    </footer>
  </section>

  <!-- Page 4: quality process flow -->
  <section class="page page-process">
    <svg class="page-art flow" width="600" height="464" viewBox="600 0 600 464">
      <defs>
        <marker id="arrow" viewBox="0 0 10 10" refX="8" refY="5" markerWidth="4" markerHeight="4" orient="auto">
          <path d="M0,0 L10,5 L0,10 z" fill="var(--line)"/>
        </marker>
      </defs>
      <polygon points="1030,0 1200,0 1200,92" fill="var(--ink)"/>
      <polygon points="1048,0 1200,0 1200,80" fill="var(--maroon)"/>

      <!-- connectors -->
      <g class="conn" marker-end="url(#arrow)">
        <path d="M868,56 V62"/>
        <path d="M868,73 V83"/>
        <path d="M868,95 V101"/>
        <path d="M843,128 H712 V156"/>
        <path d="M911,128 H900" marker-end="none"/>
        <path d="M957,130 H978"/>
        <path d="M1013,137 V151"/>
        <path d="M1013,170 V182"/>
        <path d="M980,195 H932 V164 H756"/>
        <path d="M716,170 V181"/>
        <path d="M754,188 H906 V216"/>
        <path d="M716,193 V206"/>
        <path d="M716,225 V239"/>
        <path d="M732,258 H793 V285"/>
        <path d="M716,275 V286"/>
        <path d="M716,299 V313"/>
        <path d="M716,328 V341"/>
        <path d="M716,360 V373"/>
        <path d="M716,392 V398"/>
        <path d="M793,300 V313"/>
        <path d="M793,328 V343"/>
        <path d="M793,362 V377"/>
        <path d="M818,353 H832" marker-end="none"/>
        <path d="M769,392 H745 V226"/>
        <path d="M818,402 H838 V213 H752"/>
        <path d="M906,236 V245"/>
        <path d="M889,268 H869 V288"/>
        <path d="M922,268 H940 V288"/>
        <path d="M869,302 V316"/>
        <path d="M869,334 V344"/>
        <path d="M869,380 V390 H838" marker-end="none"/>
        <path d="M940,302 V316"/>
        <path d="M940,332 V345"/>
        <path d="M940,362 V380"/>
        <path d="M963,392 H975 V227 H930"/>
      </g>
      <path d="M1013,205 V230" stroke="var(--line)" stroke-width="5" marker-end="url(#arrow)"/>
      <path d="M958,130 H973" stroke="var(--line)" stroke-width="5"/>

      <!-- top intake -->
      <polygon points="856,12 880,12 893,35 880,58 856,58 843,35" fill="var(--flow-red)"/>
      <text x="868" y="34">CUSTOMER SUPPLY</text><text x="868" y="40">MATERIAL</text>
      <rect x="828" y="62" width="80" height="11" rx="2" fill="var(--flow-red)"/>
      <text x="868" y="69.5">Warehouse Acceptance (Quantity)</text>
      <rect x="830" y="84" width="77" height="11" rx="2" fill="var(--flow-blue)"/>
      <text x="868" y="91.5">Wait For Inspection Area</text>

      <polygon points="860,101 894,101 912,128 894,155 860,155 842,128" fill="var(--flow-green)"/>
      <text class="hex-text" x="877" y="134" style="font-size:16px">IQC</text>
      <text class="label" x="828" y="126">OK</text>
      <text class="label" x="896" y="124">NO</text>

      <rect x="911" y="118" width="46" height="22" rx="4" fill="var(--flow-orange)"/>
      <text x="934" y="131">Fail Label</text>
      <rect x="979" y="124" width="68" height="13" rx="5" fill="var(--flow-teal)"/>
      <text x="1013" y="132">Wait For Improving Area</text>
      <rect x="979" y="151" width="68" height="19" rx="5" fill="var(--flow-teal)"/>
      <text x="1013" y="159">Incoming Material</text><text x="1013" y="165">Inspection Report</text>
      <rect x="979" y="182" width="68" height="23" rx="5" fill="var(--flow-teal)"/>
      <text x="1013" y="192">Communicate With</text><text x="1013" y="198">Customers</text>
      <rect x="1022" y="209" width="25" height="26" fill="var(--flow-teal)"/>
      <text x="1034.5" y="226" style="font-size:10px;font-weight:400">NO</text>
      <rect x="985" y="240" width="60" height="35" fill="var(--flow-orange)"/>
      <text x="1015" y="256" style="font-size:9px;font-weight:400">Returned</text>
      <text x="1015" y="267" style="font-size:9px;font-weight:400">Goods</text>

      <!-- pass path -->
      <rect x="678" y="157" width="77" height="13" rx="6" fill="var(--flow-green)"/>
      <text x="716" y="165.5">Pass Label</text>
      <rect x="678" y="181" width="77" height="12" rx="4" fill="var(--flow-blue)"/>
      <text x="716" y="189">Qualified Area</text>
      <rect x="680" y="206" width="71" height="20" rx="6" fill="var(--flow-blue)"/>
      <text x="716" y="218">Painting &amp; Silk Printing</text>
      <text class="label" x="758" y="212">Self Inspection</text>

      <polygon points="706,240 726,240 737,257 726,274 706,274 695,257" fill="var(--flow-red)"/>
      <text class="hex-text" x="716" y="262" style="font-size:11px">QA</text>
      <text class="label" x="692" y="272">OK</text>
      <text class="label" x="764" y="280">NO</text>

      <g fill="var(--flow-red)">
        <rect x="692" y="286" width="48" height="13" rx="1"/>
        <rect x="692" y="313" width="48" height="15" rx="1"/>
        <rect x="696" y="341" width="40" height="19" rx="1"/>
        <rect x="696" y="373" width="40" height="19" rx="1"/>
        <circle cx="716" cy="415" r="17"/>
      </g>
      <text x="716" y="294.5">Pass Label</text>
      <text x="716" y="322.5">Qualified Area</text>
      <text x="716" y="352">Package</text>
      <text x="716" y="384">Storage</text>
      <text x="716" y="417">Delivery</text>

      <g fill="var(--flow-cyan)">
        <rect x="769" y="286" width="49" height="14" rx="1"/>
        <rect x="769" y="313" width="49" height="15" rx="1"/>
        <rect x="769" y="343" width="49" height="19" rx="1"/>
        <rect x="769" y="377" width="49" height="33" rx="1"/>
      </g>
      <text x="793" y="295">Fail Label</text>
      <text x="793" y="322.5">Unqualified</text>
      <text x="793" y="351">QC Inspection</text><text x="793" y="357">Report</text>
      <text x="793" y="392">Concessions</text><text x="793" y="398">Report</text>
      <text class="label" x="755" y="375">Tiny Defect</text>
      <text class="label" x="756" y="386">OK</text>
      <text class="label" x="821" y="408">NO</text>

      <!-- fabrication path -->
      <rect x="884" y="217" width="45" height="19" rx="1" fill="var(--flow-orange)"/>
      <text x="906" y="225">Sheet Metal</text><text x="906" y="231">Fabrication</text>
      <text class="label" x="930" y="217">OK</text>
      <polygon points="896,246 916,246 927,263 916,280 896,280 885,263" fill="var(--flow-purple)"/>
      <text class="hex-text" x="906" y="268" style="font-size:11px">QC</text>
      <text class="label" x="853" y="283">OK</text>
      <text class="label" x="918" y="275">NO</text>

      <g fill="var(--flow-purple)">
        <rect x="845" y="288" width="48" height="14" rx="1"/>
        <rect x="845" y="316" width="48" height="18" rx="1"/>
        <rect x="845" y="344" width="48" height="36" rx="1"/>
      </g>
      <text x="869" y="297">Pass Label</text>
      <text x="869" y="324">Qualified Area</text><text x="869" y="330">Product</text>
      <text x="869" y="360" style="font-size:6px;font-weight:400">Semi-Finished in</text>
      <text x="869" y="368" style="font-size:6px;font-weight:400">Storage</text>
      <text class="label" x="840" y="388">OK</text>

      <g fill="var(--flow-red)">
        <rect x="916" y="288" width="48" height="14" rx="1"/>
        <rect x="916" y="316" width="48" height="16" rx="1"/>
        <rect x="916" y="345" width="48" height="17" rx="1"/>
        <rect x="916" y="380" width="48" height="24" rx="1"/>
      </g>
      <text x="940" y="297">Fail Label</text>
      <text x="940" y="326">Unqualified Area</text>
      <text x="940" y="352">QC Inspection</text><text x="940" y="358">Report</text>
      <text x="940" y="391">Concessions</text><text x="940" y="397">Report</text>
      <text class="label" x="901" y="377">Tiny Defect</text>
      <text class="label" x="975" y="376">NO</text>
    </svg>
    <footer class="footer">
      <div class="brand" style="left:12px"><span class="brand-mark"></span>Metrovex</div>
      <div class="footer-rule" style="left:92px;width:1020px - 600px;width:424px"><span></span><span></span><span></span><span></span><span></span><span></span><span></span></div>
      <div class="page-number" style="left:528px">4</div>
    </footer>
  </section>
</main>
</body>
</html>
```